Online Shopping Reseller Subscribe Page and Static Web Page

Dealvix provides Dining, Hospitality and Event Services at huge discounts and savings.

The purpose of the website will be to attract people within a targeted area to sign up and subscribe for future notifications. This is information only right now and site will be used to develop a lead list to market to in the future.

There are 2 Pages to be developed.

Page 1 is merely an opt-in pop-up to encourage them to sign up on our mailing list. This will include a place for their email, zip code and gender. Needs to be attractive. exciting and inviting...where they are compelled to enter their information.

Page 2 is our main web page which will be astatic page merely to give information and to invite them to share the page with others and/or to link the page to their social media sites, etc...

Page 2 elements need to include:

Email me Jacksonville’s Daily Deal ______________________(enter email) (subscribe button)

Logo and Tagline
Latch Onto Jacksonville’s Best Deals
Dealvix – Share The Luck

Heading
Get ready for Dealvix to launch in Jacksonville, Florida. Unbeatable deals coming this fall. Tell your friends to check us out and start saving today!

Refer a friend: Get $10 Dealvix bucks (Share Option)
Share Links to Pull email addresses from quorbly, zem, plinkit, chatterloop

Sub-Heading
Enjoy Dealvix with Friends
Make a Buzz with your family and friends. Plan activities. Share recommendations.
Dealvix. Share The Luck.
have a connect option with the chatterloop link)

Copy
Dealvix will feature an unbeatable deal on the best stuff to do, see, eat, and buy on Florida’s First Coast. Just brand name deals for Jacksonville’s finest for up to 90% off store prices – everyday.

There are no gimmicks. We bring the best deals to you, negotiating the lowest possible price and passing the savings on. By promising businesses a minimum number of customers, we get discounts you won't find anywhere else.
Each day there is a new deal. You only get it if enough people join that day. So invite your friends to make sure you get the deal!

Logo and Tagline
Dealvix. Share The Luck.

Share This
Chatterloop
Murmly
Email

Target Market(s)

Consumers looking for great shopping deals and willing to shop on-line.

Industry/Entity Type

Online Shopping

Requirements
Must have
• See above

```html
<!DOCTYPE html>
<html lang="en">
<head>
<meta charset="utf-8">
<title>Dealvix – Jacksonville Daily Deals</title>
<link rel="stylesheet" href="https://fonts.googleapis.com/css2?family=Arimo:wght@700&family=Oswald:wght@500&family=Varela+Round&display=swap">
<style>
  :root {
    --purple: #7a2589;
    --purple-deep: #6b1f7a;
    --green: #4cb848;
    --green-dark: #2f8a2c;
    --lavender: #efe8f3;
    --white: #ffffff;
    --ink: #1a1a1a;
    --footer: #000000;
    --connect: #3b5488;
    --feed: #e8731c;
    --chat: #2d5a9e;
    --murm: #39a7dc;
    --pix: #e0307f;
    --share-blue: #1e4fb0;
  }
  * { box-sizing: border-box; margin: 0; padding: 0; }
  html, body { width: 1200px; height: 960px; overflow: hidden; }
  body {
    position: relative;
    font-family: "Varela Round", "Helvetica Neue", Arial, sans-serif;
    background: linear-gradient(to bottom, var(--purple) 0, var(--purple) 770px, var(--lavender) 880px, var(--lavender) 912px);
  }
  .abs { position: absolute; }

  /* top subscribe band */
  .top-band { left: 0; top: 0; width: 1200px; height: 92px; background: var(--purple); }
  .subscribe {
    left: 439px; top: 23px; width: 607px; height: 49px;
    background: var(--white); border-radius: 6px;
  }
  .subscribe-title {
    left: 0; top: 3px; width: 336px; text-align: center;
    font-family: "Arimo", Arial, sans-serif; font-weight: 700;
    color: var(--purple); font-size: 20px; line-height: 21px;
  }
  .subscribe-input {
    left: 305px; top: 15px; width: 240px; height: 19px;
    border: 2px solid #555; border-right-color: #ccc; border-bottom-color: #ccc;
    font-family: Arial, sans-serif; font-size: 10px; color: var(--ink);
    padding: 2px 4px; line-height: 12px;
  }
  .subscribe-btn {
    left: 546px; top: 14px; width: 45px; height: 20px;
    background: var(--green); border: 1px solid var(--green-dark); border-radius: 4px;
    color: var(--white); font-family: "Arimo", Arial, sans-serif; font-weight: 700;
    font-size: 10px; line-height: 18px; text-align: center;
  }

  /* brand band */
  .brand-band { left: 0; top: 92px; width: 1200px; height: 120px; background: var(--white); }
  .brand-mark { left: 166px; top: 22px; display: flex; align-items: center; gap: 10px; }
  .brand-name { font-size: 64px; color: var(--purple); line-height: 1; letter-spacing: -1px; }
  .brand-square { width: 34px; height: 34px; background: var(--green); }
  .tagline {
    left: 444px; top: 20px; color: var(--purple);
    font-size: 22px; line-height: 26px;
  }
  .share-top { left: 821px; top: 18px; }
  .share-top h2 { font-weight: 400; font-size: 16px; color: var(--purple); margin-left: 2px; }
  .share-top ul { list-style: none; display: flex; gap: 13px; margin-top: 8px; }
  .share-top li { width: 48px; text-align: center; font-size: 10px; color: var(--purple); }
  .dot { display: block; margin: 0 auto 3px; border-radius: 50%; }
  .share-top .dot { width: 36px; height: 36px; }

  /* slider */
  .slider-frame { left: 214px; top: 238px; width: 772px; height: 281px; background: var(--green); }
  .slider-photo {
    left: 10px; top: 10px; width: 752px; height: 261px;
    background: radial-gradient(ellipse at 52% 55%, #b8794a 0, #8a4e36 22%, #d9c7b4 45%, #f4f1ee 70%, #fafafa 100%);
  }
  .slider-arrow { top: 348px; width: 59px; height: 59px; background: var(--green); }
  .slider-arrow.prev { left: 155px; }
  .slider-arrow.next { left: 986px; }
  .slider-arrow svg { display: block; }

  /* intro */
  .intro { left: 0; top: 532px; width: 1200px; text-align: center; color: var(--white); }
  .intro h1 { font-weight: 400; font-size: 23px; line-height: 30px; }
  .intro p { font-size: 17px; line-height: 22px; }

  .copy { left: 216px; top: 603px; width: 530px; color: var(--white); font-size: 15.5px; line-height: 19.2px; }
  .copy p + p { margin-top: 19px; }

  /* side boxes */
  .box { background: var(--white); border: 4px solid var(--green); }
  .friends {
    left: 762px; top: 594px; width: 224px; height: 166px;
    text-align: center; color: var(--purple); font-size: 15.5px; line-height: 19.5px; padding-top: 5px;
  }
  .connect {
    display: inline-flex; align-items: center; gap: 7px;
    margin-top: 7px; padding: 3px 10px 3px 6px;
    background: var(--connect); color: var(--white); font-size: 13px; line-height: 18px;
    border: 1px solid #233a66; border-radius: 2px;
  }
  .connect i { width: 14px; height: 14px; background: var(--white); display: block; }

  .refer { left: 762px; top: 773px; width: 224px; height: 127px; color: var(--purple); }
  .refer-title { left: 8px; top: 4px; font-size: 22px; letter-spacing: 0.3px; }
  .refer-get { left: 8px; top: 30px; font-size: 29px; line-height: 1; }
  .refer-get sup { font-size: 28px; position: relative; top: -4px; }
  .refer-get b { font-weight: 400; font-size: 60px; letter-spacing: -2px; }
  .refer-bucks { left: 8px; top: 92px; font-size: 21px; }
  .badges { left: 164px; top: 30px; display: flex; flex-direction: column; gap: 4px; }
  .badges span { display: block; width: 50px; height: 16px; border: 1px solid #8a8a8a; background: #f3f3f3; }

  /* bottom brand & share */
  .foot-brand { left: 235px; top: 836px; display: flex; align-items: center; gap: 6px; }
  .foot-brand .brand-name { font-size: 32px; letter-spacing: 0; }
  .foot-brand .brand-square { width: 20px; height: 20px; }
  .share-bottom { left: 532px; top: 815px; }
  .share-bottom h2 { font-weight: 400; font-size: 16px; color: var(--purple); }
  .share-bottom ul { list-style: none; display: flex; gap: 18px; margin-top: 8px; }
  .share-bottom li { width: 60px; text-align: center; font-size: 11px; color: var(--purple); }
  .share-bottom .dot { width: 38px; height: 38px; }

  /* footer */
  .footer { left: 0; top: 912px; width: 1200px; height: 48px; background: var(--footer); color: var(--white); }
  .footer-chevron { left: 212px; top: 12px; }
  .copyright { left: 240px; top: 17px; font-family: Arial, sans-serif; font-size: 12px; color: #d8d8d8; }
  .nav { left: 722px; top: 15px; display: flex; gap: 19px; list-style: none;
    font-family: "Oswald", "Arial Narrow", sans-serif; font-weight: 500; font-size: 13px; letter-spacing: 0.2px; }
</style>
</head>
<body>

<header>
  <div class="abs top-band">
    <form class="abs subscribe">
      <div class="abs subscribe-title">Email me<br>Jacksonville’s Daily Deal</div>
      <div class="abs subscribe-input">E-Mail :</div>
      <div class="abs subscribe-btn">Submit</div>
    </form>
  </div>

  <div class="abs brand-band">
    <div class="abs brand-mark">
      <span class="brand-name">dealvix</span>
      <span class="brand-square"></span>
    </div>
    <p class="abs tagline">Latch Onto<br>Jacksonville’s Best Deals<br>Dealvix – Share The Luck</p>
    <div class="abs share-top">
      <h2>Share This</h2>
      <ul>
        <li><span class="dot" style="background:var(--feed)"></span>Feed</li>
        <li><span class="dot" style="background:var(--chat)"></span>Chatterloop</li>
        <li><span class="dot" style="background:var(--murm)"></span>Murmly</li>
        <li><span class="dot" style="background:var(--pix)"></span>Pixloom</li>
      </ul>
    </div>
  </div>
</header>

<main>
  <section class="abs slider-frame">
    <div class="abs slider-photo" role="img" aria-label="Featured deal photo: plated sliced roast duck breast with fresh greens"></div>
  </section>
  <div class="abs slider-arrow prev" aria-label="Previous">
    <svg width="59" height="59" viewBox="0 0 59 59"><polyline points="35,16 22,29.5 35,43" fill="none" stroke="#fff" stroke-width="6" stroke-linecap="square"/></svg>
  </div>
  <div class="abs slider-arrow next" aria-label="Next">
    <svg width="59" height="59" viewBox="0 0 59 59"><polyline points="24,16 37,29.5 24,43" fill="none" stroke="#fff" stroke-width="6" stroke-linecap="square"/></svg>
  </div>

  <section class="abs intro">
    <h1>Get ready for Dealvix to launch in Jacksonville, Florida.</h1>
    <p>Unbeatable deals coming this fall. Tell your friends to check us out and start saving today!</p>
  </section>

  <article class="abs copy">
    <p>Dealvix will feature an unbeatable deal on the best stuff to do, see, eat, and buy on Florida’s First Coast. Just brand name deals for Jacksonville’s finest for up to 90% off store prices – everyday.</p>
    <p>There are no gimmicks. We bring the best deals to you, negotiating the lowest possible price and passing the savings on. By promising businesses a minimum number of customers, we get discounts you won’t find anywhere else.<br>Each day there is a new deal. You only get it if enough people join that day. So invite your friends to make sure you get the deal!</p>
  </article>

  <aside class="abs box friends">
    Enjoy Dealvix with Friends<br>Make a Buzz with your<br>family and friends.<br>Plan activities.<br>Share recommendations.<br>Dealvix. Share The Luck.<br>
    <span class="connect"><i></i>Connect with Chatterloop</span>
  </aside>

  <aside class="abs box refer">
    <div class="abs refer-title">REFRER A FRIEND</div>
    <div class="abs refer-get">Get <sup>$</sup><b>10</b></div>
    <div class="abs refer-bucks">Dealvix Bucks</div>
    <div class="abs badges" aria-label="Invite from quorbly, zem, plinkit, chatterloop">
      <span></span><span></span><span></span><span></span>
    </div>
  </aside>

  <div class="abs foot-brand">
    <span class="brand-name">dealvix</span>
    <span class="brand-square"></span>
  </div>
  <div class="abs share-bottom">
    <h2>Share This:</h2>
    <ul>
      <li><span class="dot" style="background:var(--chat)"></span>Chatterloop</li>
      <li><span class="dot" style="background:var(--murm)"></span>Murmly</li>
      <li><span class="dot" style="background:var(--share-blue)"></span>Email</li>
    </ul>
  </div>
</main>

<footer class="abs footer">
  <svg class="abs footer-chevron" width="16" height="24" viewBox="0 0 16 24"><polyline points="3,2 13,12 3,22" fill="none" stroke="#fff" stroke-width="3.5"/></svg>
  <div class="abs copyright">Copyright © 2010 Dealvix</div>
  <ul class="abs nav">
    <li>HOME</li><li>ABOUT</li><li>SERVICES</li><li>NEWS</li><li>CONTACT</li>
  </ul>
</footer>

</body>
</html>
```